Enhance existing websites

Hello,

With my very limited web design knowledge I have designed my own websites...
Trailquote.example
Rovervalue.example

Whilst I have been very happy with the response I have received I feel the sites need enhancing. Here is what I would like to change..

1, Place a shadow around the whole pages outline so it has a 3d effect with a better background colour.

2, Improve the 'Request a valuation' tab so it stands out, maybe to also insert a curved arrow(s) to direct customer to click 'request a valuation' . Naturally this would need to be done on each page.

3, The testimonials of the 'what customers say' to change every few seconds.

4, The front page image to change every few seconds to a image of my choice.

5, any other suggestions you feel would benefit my site (obviously willing to pay extra for this and within this site)

6, given my limited knowledge my html code will surely need tidying also

7, if possible any changes not to affect my very good google ratings.

Price paid is for both sites as they're practically identical.

Thanks in advance

Glen

```html
<!DOCTYPE html>
<html lang="en">
<head>
<meta charset="utf-8">
<title>Trailquote.example – Sell your caravan quickly and securely</title>
<link href="https://fonts.googleapis.com/css2?family=Ubuntu:wght@300;400;500;700&family=Ubuntu+Condensed&family=PT+Sans+Narrow:wght@700&display=swap" rel="stylesheet">
<style>
:root{
  --orange:#e8902a;
  --orange-dark:#d27c1b;
  --blue:#4a67a6;
  --blue-soft:#6f8ccb;
  --text:#333;
  --muted:#555;
  --rule:#e2e2e2;
  --footer:#0d0d0d;
}
*{margin:0;padding:0;box-sizing:border-box}
html,body{width:871px;height:1200px;overflow:hidden}
body{position:relative;background:#fff;font-family:"Ubuntu",sans-serif;color:var(--text)}
.abs{position:absolute}

.site-header{left:0;top:0;width:871px;height:56px;background:#fff}
.brand{left:82px;top:9px}
.brand-name{font-family:"Ubuntu",sans-serif;font-weight:500;font-size:23px;color:var(--blue);letter-spacing:.3px;line-height:26px}
.brand-tag{font-size:9px;color:#222;margin-left:4px}
.phone{right:103px;top:20px;font-family:"Ubuntu Condensed",sans-serif;font-size:19px;color:var(--orange)}

.main-nav{left:0;top:56px;width:871px;height:37px;background:linear-gradient(var(--orange),var(--orange-dark))}
.main-nav ul{list-style:none;position:absolute;left:93px;top:10px;display:flex;gap:16px}
.main-nav a{color:#fff;text-decoration:none;font-family:"Ubuntu Condensed",sans-serif;font-size:13px}
.search{left:593px;top:61px;width:170px;height:27px;background:#fff;border-radius:3px;font-size:9px;color:#999;padding:8px 10px}
.search svg{position:absolute;right:7px;top:6px}

.hero-band{left:0;top:93px;width:871px;height:373px;background:linear-gradient(#fff 0%,#f1f1f1 40%,#e4e4e4 100%)}
.hero{left:98px;top:106px;width:675px;height:274px;border-radius:3px;background:linear-gradient(180deg,#5d86b8 0%,#a6bfd8 35%,#7b8a6a 52%,#46688a 62%,#9a8a6a 80%,#4a4a4a 100%);box-shadow:0 2px 6px rgba(0,0,0,.3)}
.slider-dots{left:120px;top:336px}
.social{left:830px;width:24px;height:24px;border-radius:3px;color:#fff;font-size:9px;font-weight:500;display:flex;align-items:center;justify-content:center;background:var(--blue-soft)}

.tagline{left:109px;top:419px;font-family:"PT Sans Narrow",sans-serif;font-weight:700;font-size:21px;color:var(--blue);letter-spacing:.2px}
.cta{left:497px;top:413px;width:241px;height:37px;background:var(--blue-soft);color:#fff;font-family:"Ubuntu Condensed",sans-serif;font-size:14px;display:flex;align-items:center;justify-content:center;border-radius:2px;box-shadow:0 1px 3px rgba(0,0,0,.2)}
.cta-arrow{left:458px;top:432px}

.benefits{left:100px;top:488px;width:440px;font-size:10.5px;color:#222}
.benefit{position:absolute;white-space:nowrap}
.benefit::before{content:"»";margin-right:5px;color:#555}
.copy{left:104px;top:586px;width:438px;font-size:9.3px;line-height:17.5px;color:#333;font-weight:300}
.copy p{margin-bottom:10px}
.copy strong{font-weight:400}
.photo{left:106px;top:846px;width:436px;height:156px;border-radius:3px;background:linear-gradient(180deg,#6f8b4a 0%,#4d6a2c 45%,#dcdcd8 62%,#9fb06c 80%,#5a7a2e 100%)}
.carousel-btn{width:24px;height:24px;border-radius:50%;background:#e6e6e6;color:#777;font-size:13px;display:flex;align-items:center;justify-content:center;top:1045px}
.maker{font-family:"Ubuntu",sans-serif;font-weight:700;font-size:8.5px;color:var(--blue);white-space:nowrap}

.sidebar-rule{left:558px;top:466px;width:4px;height:688px;background:linear-gradient(90deg,rgba(0,0,0,.06),transparent)}
.side-title{left:583px;top:475px;font-family:"PT Sans Narrow",sans-serif;font-weight:700;font-size:20px;color:var(--blue)}
.side-intro{left:584px;top:508px;width:200px;font-size:9.5px;font-weight:500;line-height:18px;color:#555}
.towns{left:584px;top:549px;list-style:none;font-size:9.5px;line-height:13px;color:#222;font-weight:300}
.map{left:668px;top:568px;width:88px;height:144px;background:linear-gradient(160deg,#c8d0e6,#d8626a 55%,#3a4f9a)}
.email{left:581px;top:760px;font-size:14.5px;color:var(--blue-soft);font-weight:300}
.hr{left:568px;width:190px;height:2px;background:linear-gradient(90deg,transparent,var(--rule) 10%,var(--rule) 90%,transparent)}
.say{left:581px;top:795px;font-size:14.5px;color:var(--orange)}
.quote{left:590px;width:160px;font-size:9.4px;line-height:13px;color:#333;font-weight:300}
.quote-mark{font-family:Georgia,serif;font-size:15px;color:#888;line-height:0}
.who{font-size:9.8px;color:#222;font-weight:300;white-space:nowrap}

.site-footer{left:0;top:1154px;width:871px;height:46px;background:var(--footer);color:#ddd;font-size:9.5px;font-weight:300}
.site-footer ul{list-style:none;position:absolute;left:106px;top:17px;display:flex;gap:13px}
.site-footer .addr{position:absolute;left:495px;top:17px}
.site-footer .code{position:absolute;left:823px;top:17px}
</style>
</head>
<body>

<header class="site-header abs">
  <div class="brand abs">
    <div class="brand-name">trailquote.example</div>
    <div class="brand-tag">The UK's largest buyer of touring caravans</div>
  </div>
  <div class="phone abs">Call us on : 0800 000 4417</div>
</header>

<nav class="main-nav abs">
  <ul>
    <li><a href="#">Home</a></li>
    <li><a href="#">How it works</a></li>
    <li><a href="#">FAQ's</a></li>
    <li><a href="#">Contact Us</a></li>
  </ul>
</nav>
<div class="search abs">Search
  <svg width="15" height="15" viewBox="0 0 15 15"><circle cx="6" cy="6" r="4.5" fill="none" stroke="#999" stroke-width="1.4"/><line x1="9.3" y1="9.3" x2="14" y2="14" stroke="#999" stroke-width="1.8"/></svg>
</div>

<section class="hero-band abs"></section>
<div class="hero abs" role="img" aria-label="Photo of a white motorhome driving along a coastal road beneath mountains"></div>
<svg class="slider-dots abs" width="92" height="20" viewBox="0 0 92 20">
  <path d="M10 2 L2 10 L10 18 M16 2 L8 10 L16 18" fill="none" stroke="#fff" stroke-width="1.6"/>
  <circle cx="31" cy="10" r="5" fill="#fff"/><circle cx="46" cy="10" r="5" fill="#fff"/><circle cx="61" cy="10" r="5" fill="#fff"/>
  <path d="M76 2 L84 10 L76 18 M82 2 L90 10 L82 18" fill="none" stroke="#fff" stroke-width="1.6"/>
</svg>

<a class="social abs" style="top:122px" aria-label="Postboard">PB</a>
<a class="social abs" style="top:151px" aria-label="Chirper">CH</a>
<a class="social abs" style="top:180px;background:var(--orange)" aria-label="Linkly">LK</a>

<h1 class="tagline abs">SELL YOUR CARAVAN QUICKLY AND SECURELY</h1>
<svg class="cta-arrow abs" width="50" height="24" viewBox="0 0 50 24">
  <path d="M2 20 C16 25 32 20 46 6" fill="none" stroke="#222" stroke-width="1.2"/>
  <path d="M40 6 L47 5 L45 12" fill="none" stroke="#222" stroke-width="1.2"/>
</svg>
<a class="cta abs" href="#">Request a FREE Caravan Valuation</a>

<ul class="benefits abs">
  <li class="benefit" style="left:0;top:0">Genuine online or verbal offer to purchase</li>
  <li class="benefit" style="left:242px;top:2px">Excellent prices offered and paid</li>
  <li class="benefit" style="left:0;top:35px">No admin fees or hidden charges</li>
  <li class="benefit" style="left:242px;top:37px">Friendly professional, no hassle service</li>
  <li class="benefit" style="left:0;top:70px">Instant cash or faster payment bank transfer</li>
</ul>

<div class="copy abs">
  <p>Selling your caravan to trailquote.example saves you the usual headaches and costs associated with selling a caravan, not to mention the potential risks involved. All you need to do is either call us on the freephone number provided, or click the button above and complete our online request form with details of your caravan. We will get back to you as soon as possible with a price and a no obligation offer to buy your caravan. If you accept our offer, we'll contact you to collect your caravan at your convenience - free of charge.</p>
  <p>It is our aim to make the process of selling your caravan completely straightforward and hassle-free. From your initial enquiry, to having your caravan sold with money in your bank account or cash in your hand, can take less than 24 hours. We have even managed to complete some transactions the very same day the offer was received.</p>
  <p>Remember, there are no hidden charges for our service and you are not under any obligation to accept our offer. You really do have nothing to lose by simply finding out how much we can pay for your caravan.</p>
</div>

<div class="photo abs" role="img" aria-label="Photo of touring caravans with awnings pitched on a grassy campsite among trees"></div>

<div class="carousel-btn abs" style="left:111px">«</div>
<div class="carousel-btn abs" style="left:497px">»</div>
<span class="maker abs" style="left:162px;top:1033px">Moonvale</span>
<span class="maker abs" style="left:234px;top:1034px">Highroad</span>
<span class="maker abs" style="left:298px;top:1036px">Lumina</span>
<span class="maker abs" style="left:362px;top:1036px">Fenwick</span>
<span class="maker abs" style="left:420px;top:1037px">Eastwind</span>
<span class="maker abs" style="left:160px;top:1072px">Lakeshore</span>
<span class="maker abs" style="left:228px;top:1072px">Wayfarer</span>
<span class="maker abs" style="left:298px;top:1073px">Adara</span>
<span class="maker abs" style="left:360px;top:1073px">Rolling Co</span>
<span class="maker abs" style="left:422px;top:1071px">Dunmore</span>

<div class="sidebar-rule abs"></div>
<h2 class="side-title abs">FREE COLLECTION</h2>
<p class="side-intro abs">Below are some examples of&nbsp; of the areas we cover ...</p>
<ul class="towns abs">
  <li>Birmingham</li><li>Cambridge</li><li>Chelmsford</li><li>Chichester</li><li>Chester</li><li>Exeter</li><li>Hertford</li><li>Leominster</li><li>Lincoln</li><li>Maidstone</li><li>Manchester</li><li>Norwich</li><li>Swansea</li><li>Truro</li><li>Wakefield</li>
</ul>
<div class="map abs" role="img" aria-label="Map of the United Kingdom filled with the Union flag"></div>
<a class="email abs">info@trailquote.example</a>
<div class="hr abs" style="top:786px"></div>
<h3 class="say abs">What our customers say....</h3>

<blockquote class="quote abs" style="top:826px"><span class="quote-mark">“</span>It was a pleasure to meet you Glen, thank you for a stress free sale of our caravan. I hope she goes to a good home. <span class="quote-mark">”</span></blockquote>
<span class="who abs" style="left:591px;top:891px">G. Hollins</span><span class="who abs" style="left:670px;top:891px">- Northway Vista</span>
<div class="hr abs" style="top:916px"></div>
<blockquote class="quote abs" style="top:936px"><span class="quote-mark">“</span>Just a quick note to say thank you for the excellent service you provided in purchasing my Brisk caravan <span class="quote-mark">”</span></blockquote>
<span class="who abs" style="left:591px;top:995px">B. Marlow</span><span class="who abs" style="left:669px;top:995px">- Brisk Charm</span>
<div class="hr abs" style="top:1026px"></div>
<blockquote class="quote abs" style="top:1046px"><span class="quote-mark">“</span>I wanted to sell my caravan fast and you made it so easy. We wouldn't hesitate in recommending you to friends. <span class="quote-mark">”</span></blockquote>
<span class="who abs" style="left:589px;top:1105px">T. Ashby</span><span class="who abs" style="left:669px;top:1105px">- Lakeshore Arrow</span>

<footer class="site-footer abs">
  <ul><li>Home</li><li>How it works</li><li>FAQ's</li><li>Contact Us</li></ul>
  <span class="addr">Trailquote.example - Mill Lane&nbsp; - Oakridge&nbsp; - Essex CM00 1AA</span>
  <span class="code">M1</span>
</footer>

</body>
</html>
```